Brimvale Website

I need a design of homepage for a health and wellness center. We considers self to be young and fresh and want something along that design. We want a main picture/logo/design (or all three), and underneath that 4 pictures to depict what services we do. The four services are Orthopedic Rehab, Neurological Rehab, Speech Pathology and Float. I have attached our logo, and some pictures that might be helpful, but the pictures don't have to be included. Here is an example of what I would like it look. http://pixelbazaar.net/web-design/contests/lumotrek-website-design-needed-more-work-come-submit-517306/entries/84126759

```html
<!DOCTYPE html>
<html lang="en">
<head>
<meta charset="utf-8">
<title>Brimvale Center for Health + Wellness</title>
<link href="https://fonts.googleapis.com/css2?family=Source+Sans+3:wght@400;600&display=swap" rel="stylesheet">
<style>
:root{
  --sage:#86b5a7;
  --aqua:#77c6be;
  --aqua-dark:#5fa9a1;
  --lime:#a8c13c;
  --ink:#8a9296;
  --ink-strong:#7d8589;
  --mist:#dcedea;
  --hero:#d3e8e2;
  --paper:#fafcfb;
  --white:#ffffff;
}
*{margin:0;padding:0;box-sizing:border-box}
html,body{width:1024px;height:1200px;overflow:hidden}
body{background:var(--paper);font-family:"Source Sans 3",sans-serif;color:var(--ink);position:relative}
.abs{position:absolute}
.topline{left:0;top:0;width:1024px;height:3px;background:var(--sage)}
.site-header{left:0;top:3px;width:1024px;height:77px;background:var(--white);border-bottom:1px solid #c9d3d1}
.brand{left:138px;top:22px;display:flex;align-items:center;gap:10px}
.brand-mark{width:34px;height:34px;border-radius:50%;background:var(--lime)}
.brand-name{font-size:34px;font-weight:400;color:var(--sage);letter-spacing:1px}
.social-top{top:10px;display:flex;gap:11px;left:669px}
.social-top span{width:19px;height:19px;border-radius:2px;background:var(--sage)}
.account{left:760px;top:3px;width:128px;height:28px;background:var(--sage);color:var(--white);font-size:10.5px;display:flex;align-items:center;justify-content:center;gap:8px}
.main-nav{right:139px;top:50px;display:flex;font-size:13px;color:var(--sage);letter-spacing:.5px}
.main-nav span+span::before{content:"|";margin:0 18px;font-size:10px;vertical-align:1px}
.hero{left:0;top:80px;width:1024px;height:386px;background:radial-gradient(ellipse at 68% 45%,#ffffff 0%,#eaf4f1 35%,var(--hero) 75%);border-bottom:1px solid #c9d3d1}
.hero-art{left:0;top:0;width:480px;height:386px;background:linear-gradient(135deg,#a9c66b 0%,#9ebf80 40%,#88b5a7 75%,#8ab7aa 100%);opacity:.55}
.hero-copy{left:504px;top:80px;width:400px}
.hero-copy h1{font-weight:400;font-size:29px;color:var(--sage);margin-top:80px;line-height:1}
.hero-copy h2{font-weight:400;font-size:14px;color:var(--lime);margin-top:14px}
.hero-copy p{font-size:10.5px;line-height:17.6px;margin-top:16px;padding-left:2px}
.btn{display:flex;align-items:center;justify-content:center;background:var(--aqua);color:var(--white);box-shadow:0 3px 0 var(--aqua-dark);border-radius:2px}
.hero-btn{margin-top:26px;width:160px;height:40px;font-size:14px}
.intro{left:0;top:490px;width:1024px;text-align:center}
.intro h3{font-size:13.5px;font-weight:600;color:var(--ink)}
.intro p{font-size:10.5px;line-height:17.6px;width:440px;margin:13px auto 0}
.service{top:591px;width:176px;text-align:center}
.service .disc{width:168px;height:168px;border-radius:50%;background:var(--mist);margin:0 auto;display:flex;align-items:center;justify-content:center}
.service .disc i{display:block;width:72px;height:72px;border-radius:40%;background:var(--sage);opacity:.85}
.service h4{font-size:13.5px;font-weight:600;color:var(--ink-strong);margin-top:19px}
.service p{font-size:10.5px;line-height:16.8px;margin-top:20px}
.service .btn{width:160px;height:40px;margin:20px auto 0;font-size:10.5px}
.sec-title{font-size:13.5px;font-weight:600;color:var(--ink)}
.sec-title b{color:var(--aqua);font-weight:600}
.about-title{left:135px;top:972px}
.about-photo{left:136px;top:1002px;width:176px;height:100px;background:linear-gradient(90deg,#6f8a6c 0%,#b89a8e 45%,#e9ecea 100%);border-radius:2px}
.about-text{left:328px;top:1000px;width:240px;font-size:10.5px;line-height:17.4px}
.why-title{left:582px;top:972px}
.why-list{left:583px;top:1005px;list-style:none;font-size:10.5px}
.why-list li{display:flex;align-items:center;height:17px;margin-bottom:11.7px}
.why-list .tick{width:17px;height:17px;background:var(--aqua);display:flex;align-items:center;justify-content:center;margin-right:15px}
.site-footer{left:0;top:1155px;width:1024px;height:45px;background:var(--sage);color:#eef6f3;font-size:10.5px}
.foot-nav{left:138px;top:15px;display:flex}
.foot-nav span+span::before{content:"|";margin:0 13px}
.copyright{left:582px;top:15px}
.social-foot{left:786px;top:10px;display:flex;gap:13px}
.social-foot span{width:26px;height:25px;border-radius:3px;background:var(--white)}
</style>
</head>
<body>
<div class="abs topline"></div>
<header class="abs site-header">
  <div class="abs brand"><span class="brand-mark"></span><span class="brand-name">Brimvale</span></div>
  <div class="abs social-top"><span></span><span></span><span></span></div>
  <div class="abs account"><span>REGISTER</span><span>|</span><span>LOGIN</span></div>
  <nav class="abs main-nav"><span>HOME</span><span>SERVICES</span><span>ABOUT</span><span>CONTACT</span></nav>
</header>

<section class="abs hero">
  <div class="abs hero-art" role="img" aria-label="Large green and sage leaf illustration"></div>
  <div class="abs hero-copy" style="top:0">
    <h1>Simplicity &amp; consistency.</h1>
    <h2>Dignissim ut, platea quis! Penatibus natoque.</h2>
    <p>De nombreuses suites logicielles de mise en page ou éditeurs de sites Web ont fait du Lorem Ipsum leur faux texte par défaut, et une recherche pour 'Lorem Ipsum' vous conduira vers de nombreux sites. Lorem Ipsum sur Internet tendent</p>
    <div class="btn hero-btn">Read More</div>
  </div>
</section>

<section class="abs intro">
  <h3>BLOCKQUOTE</h3>
  <p>Cras consequat porttitor tincidunt. Praesent eu tincidunt lacus. Donec ut neque vitae erat congue venenatis. Duis hendrerit lacinia leo in dignissim. Aliquam erat volutpat. Sed</p>
</section>

<article class="abs service" style="left:137px">
  <div class="disc" role="img" aria-label="Orthopedic rehab illustration"><i></i></div>
  <h4>Orthopedic Rehab</h4>
  <p>Ut eleifend libero sed neque rhoncus consequat. Maecenas tincidunt, augue et rutrum mattis</p>
  <div class="btn">read more</div>
</article>
<article class="abs service" style="left:327px">
  <div class="disc" role="img" aria-label="Neurological rehab illustration"><i></i></div>
  <h4>Neurological Rehab</h4>
  <p>Ut eleifend libero sed neque rhoncus consequat. Maecenas tincidunt, augue et rutrum mattis</p>
  <div class="btn">read more</div>
</article>
<article class="abs service" style="left:521px">
  <div class="disc" role="img" aria-label="Speech pathology illustration"><i></i></div>
  <h4>Speech Pathology</h4>
  <p>Ut eleifend libero sed neque rhoncus consequat. Maecenas tincidunt, augue et rutrum mattis</p>
  <div class="btn">read more</div>
</article>
<article class="abs service" style="left:711px">
  <div class="disc" role="img" aria-label="Float therapy water illustration"><i></i></div>
  <h4>Float</h4>
  <p>Ut eleifend libero sed neque rhoncus consequat. Maecenas tincidunt, augue et rutrum mattis</p>
  <div class="btn">read more</div>
</article>

<h3 class="abs sec-title about-title">ABOUT <b>BRIMVALE</b></h3>
<div class="abs about-photo" role="img" aria-label="Photo of the center's reception area behind leaves"></div>
<p class="abs about-text">Cras consequat porttitor tincidunt. Praesent eu tincidunt lacus. Donec ut neque vitae erat congue venenatis. Duis hendrerit lacinia leo in dignissim. Aliquam erat volutpat. Seddignissim hendrerit nibh, quis faucibus erat cursus eget. Integer porta nisl vitae felis rutrum ut mollis felis congue.</p>

<h3 class="abs sec-title why-title">WHY <b>CHOOSE US</b></h3>
<ul class="abs why-list">
  <li><span class="tick"><svg width="6" height="8" viewBox="0 0 6 8"><path d="M1 1l3 3-3 3" stroke="#fff" stroke-width="1.6" fill="none"/></svg></span>Le Aorem Ipsum ainsi obtenu ne contient aucune</li>
  <li><span class="tick"><svg width="6" height="8" viewBox="0 0 6 8"><path d="M1 1l3 3-3 3" stroke="#fff" stroke-width="1.6" fill="none"/></svg></span>Répétition secolilorem nunc.adipiscing</li>
  <li><span class="tick"><svg width="6" height="8" viewBox="0 0 6 8"><path d="M1 1l3 3-3 3" stroke="#fff" stroke-width="1.6" fill="none"/></svg></span>Contrairement à une opinion répandue, le Lorem</li>
  <li><span class="tick"><svg width="6" height="8" viewBox="0 0 6 8"><path d="M1 1l3 3-3 3" stroke="#fff" stroke-width="1.6" fill="none"/></svg></span>Ipsum n'est pas at erat in purus aliquet</li>
</ul>

<footer class="abs site-footer">
  <nav class="abs foot-nav"><span>Home</span><span>About</span><span>Services</span><span>Contact</span></nav>
  <div class="abs copyright">© 2014 Brimvale ~ &nbsp;All rights reserved.</div>
  <div class="abs social-foot"><span></span><span></span><span></span></div>
</footer>
</body>
</html>
```